Rent a Velvet needs a Stunning web design

Rent a Velvet is an upmarket agency in Sydney that has lingerie waitresses for events.

Rent a Velvet is looking for a website design that is as sexy and sophisticated as the ladies who work for them!

The design mustn't be cluttered, tacky or pornographic. What I'm looking for is something better than the industry leader www.glimmerdolls.com.au Something classy, sexy and different.

When designing please suggest a CMS, we already use wordpress but are open to suggestions.

We will need a home page that incorporates a feed from a blog and/or social media (please make suggestions and use your discretion as a designer, however we'd like to approve what goes into the feed before it goes in.) The home page could also have a list of our services, but if not we will need a services page. Our Services include:
Lingerie waitressing at events
Lingerie waitresses to help dress the groom pre wedding.
Bucks parties

We have a logo that we'd like incorporated into the design and have attached it.

We will also need a portfolio page for the ladies, This is not to be cluttered, tacky or pornographic. It needs to be classy.

We will also need a "Contact us" page and were thinking that this could potentially also be a "Ask for a quote on your event" page. I.e. have a regular "Contact us" form but have alternate fields if they tick the "I want a quote" box. Alternatively you could have two parts to the contact us page. One that is a regular form and one that has a "Your requirements" box.

Again please use your discretion when designing these, if it's too cluttered it won't work. If it looks tacky, don't do it. If you have suggestions make them.

Target Market(s)

Males between the ages of 18 - 45

Industry/Entity Type

Industry

Requirements
Must have
• Must incorporate our logo.

```html
<!DOCTYPE html>
<html lang="en">
<head>
<meta charset="utf-8">
<title>Rent a Velvet</title>
<link rel="stylesheet" href="https://fonts.googleapis.com/css2?family=Arimo:wght@400;700&family=Oswald:wght@600&display=swap">
<style>
  :root {
    --bg: #151515;
    --stripe: #1d1d1d;
    --red: #e0173f;
    --red-light: #ff5a78;
    --white: #f2f2f2;
    --grey: #9a9a9a;
    --rule: #3a3a3a;
    --nav-top: #2a2a2a;
    --nav-bottom: #161616;
  }
  * { box-sizing: border-box; margin: 0; padding: 0; }
  html, body { width: 1198px; height: 1200px; overflow: hidden; }
  body {
    background: var(--bg) repeating-linear-gradient(to bottom, var(--stripe) 0 2px, var(--bg) 2px 4px);
    font-family: "Arimo", Arial, sans-serif;
    color: var(--white);
    position: relative;
  }
  .brand {
    position: absolute; left: 112px; top: 62px;
    display: flex; align-items: center; gap: 14px;
    font-size: 44px; font-weight: 700; color: var(--red); letter-spacing: -0.5px;
  }
  .brand-dot { width: 22px; height: 22px; border-radius: 50%; background: var(--white); }
  .account {
    position: absolute; left: 808px; top: 36px;
    display: flex; align-items: center; gap: 10px;
    font-size: 13px; color: #cfcfcf;
  }
  .account .sep { color: #777; }
  .social { position: absolute; top: 33px; left: 1080px; display: flex; gap: 11px; }
  .social span { width: 30px; height: 30px; border-radius: 4px; background: #d8d8d8; }
  .search { position: absolute; left: 869px; top: 103px; display: flex; gap: 12px; }
  .search-field {
    width: 211px; height: 36px; border: 1px solid #666; background: #111;
    color: #999; font-size: 14px; padding: 9px 16px;
  }
  .search-button { width: 59px; height: 36px; background: var(--red); display: flex; align-items: center; justify-content: center; }
  .main-nav {
    position: absolute; left: 47px; top: 170px; width: 1104px; height: 71px;
    background: linear-gradient(var(--nav-top), var(--nav-bottom));
  }
  .main-nav a {
    position: absolute; top: 25px; font-size: 18px; letter-spacing: 1px;
    color: var(--white); text-decoration: none;
  }
  .main-nav a.active { color: var(--red); }
  .hero-photo {
    position: absolute; left: 117px; top: 288px; width: 611px; height: 299px;
    background: radial-gradient(ellipse at 55% 55%, #7a5440 0%, #3a2a22 35%, rgba(21,21,21,0) 70%);
  }
  .hero-title {
    position: absolute; left: 797px; top: 276px;
    font-family: "Oswald", "Arial Narrow", sans-serif; font-weight: 600;
    font-size: 88px; line-height: 1; color: var(--red); letter-spacing: 1px;
  }
  .hero-subtitle {
    position: absolute; left: 799px; top: 362px;
    font-size: 36px; font-weight: 700; font-style: italic; color: var(--grey); letter-spacing: 1px;
  }
  .read-more, .read-more-reflection {
    position: absolute; left: 801px; width: 235px; height: 71px; border-radius: 36px;
    background: linear-gradient(var(--red-light), var(--red) 55%, #b80f30);
    font-size: 32px; font-weight: 700; color: #1a1a1a;
    display: flex; align-items: center; justify-content: center;
  }
  .read-more { top: 466px; }
  .read-more-reflection {
    top: 539px; transform: scaleY(-1); opacity: 0.28;
    -webkit-mask-image: linear-gradient(to top, #000, transparent 70%);
            mask-image: linear-gradient(to top, #000, transparent 70%);
  }
  .slider-dots { position: absolute; left: 802px; top: 648px; display: flex; gap: 7px; }
  .slider-dots span { width: 24px; height: 24px; border-radius: 50%; background: radial-gradient(circle at 40% 35%, #777, #3a3a3a); }
  .slider-dots span.current { background: radial-gradient(circle at 40% 35%, #ff5a78, var(--red)); }
  .divider { position: absolute; left: 47px; top: 725px; width: 1104px; height: 1px; background: #555; }
  .footer-col { position: absolute; top: 764px; }
  .footer-col h2 {
    font-size: 22px; font-weight: 400; color: var(--red);
    padding-bottom: 10px; border-bottom: 1px solid var(--rule);
  }
  .footer-col li, .footer-col p {
    list-style: none; font-size: 13.5px; line-height: 1.18; color: var(--red);
  }
  .links { left: 48px; width: 304px; }
  .links li { height: 36.4px; padding-top: 11px; border-bottom: 1px solid var(--rule); }
  .links li:last-child { border-bottom: none; }
  .philosophy { left: 393px; width: 388px; }
  .philosophy li { padding: 12px 0 10px; border-bottom: 1px solid var(--rule); }
  .philosophy li.tall { padding: 20px 0 16px; }
  .philosophy li:last-child { border-bottom: none; }
  .modus { left: 823px; width: 328px; }
  .modus p { padding: 12px 0; border-bottom: 1px solid var(--rule); line-height: 1.5; }
  .modus p.plain { border-bottom: none; }
</style>
</head>
<body>
  <header>
    <div class="brand"><span>Rent a Velvet</span><span class="brand-dot"></span></div>
    <div class="account">
      <svg width="24" height="24" viewBox="0 0 24 24" aria-hidden="true"><circle cx="12" cy="7" r="6" fill="#aaa"/><path d="M0 24c0-7 5-10 12-10s12 3 12 10z" fill="#aaa"/></svg>
      <span>My Account</span><span class="sep">|</span><span>Login or Register</span>
    </div>
    <div class="social"><span></span><span></span></div>
    <form class="search">
      <div class="search-field">Search girls</div>
      <div class="search-button">
        <svg width="26" height="26" viewBox="0 0 26 26" aria-hidden="true"><circle cx="15" cy="10" r="7.5" fill="none" stroke="#111" stroke-width="4"/><line x1="10" y1="15" x2="3" y2="22" stroke="#111" stroke-width="5" stroke-linecap="round"/></svg>
      </div>
    </form>
    <nav class="main-nav">
      <a class="active" href="#" style="left:75px">HOME</a>
      <a href="#" style="left:178px">SEMPER</a>
      <a href="#" style="left:307px">NUSQUAM</a>
      <a href="#" style="left:450px">LEGERE</a>
      <a href="#" style="left:574px">ELECTRAM</a>
      <a href="#" style="left:726px">OMNIUS REBUS</a>
      <a href="#" style="left:920px">CONTACT</a>
    </nav>
  </header>

  <section class="hero">
    <div class="hero-photo" role="img" aria-label="Photo of a model in black lingerie reclining on a dark floor"></div>
    <h1 class="hero-title">CAUSA</h1>
    <p class="hero-subtitle">PRINCIPES</p>
    <a class="read-more">Read more</a>
    <div class="read-more-reflection" aria-hidden="true">Read more</div>
    <div class="slider-dots"><span></span><span class="current"></span><span></span><span></span></div>
  </section>

  <div class="divider"></div>

  <footer>
    <div class="footer-col links">
      <h2>Oblique Elaboraret</h2>
      <ul>
        <li>Reformidans Iuvaret</li>
        <li>Consequuntur</li>
        <li>Ullamcorper Essent</li>
        <li>Gloriatur</li>
        <li>Primis Scriptorem</li>
        <li>Nulla</li>
        <li>Reformidans</li>
        <li>Consequuntur</li>
        <li>Gloriatur Dicam</li>
      </ul>
    </div>
    <div class="footer-col philosophy">
      <h2>Legimus Philosophia</h2>
      <ul>
        <li>Laboramus prodesset instructior: Ex duo, eum at minim accusam</li>
        <li class="tall">Ei usu: Qualisque Suscipiantur</li>
        <li>Cu ferri ornatus consequat qui, ea case modus perpetua nam, qui no agam docendi noluisse</li>
        <li class="tall">Eum hendrerit consequat: no sea sumo</li>
        <li>Ex duo, eum at minim accusam. Ei usu qualisque suscipiantur, cu his veniam honestatis. Cu ferri ornatus consequat qui, ea case modus perpetua nam</li>
        <li class="tall">Laboramus prodesset instructior: Ex duo, eum at minim accusam</li>
        <li class="tall">Ei usu: Qualisque Suscipiantur</li>
      </ul>
    </div>
    <div class="footer-col modus">
      <h2>Modus</h2>
      <p class="plain">Modo scriptorem an per, modus consul partem duo cu, falli saperet mandamus in vel. Ius insolens mandamus necessitatibus ad, ei quo percipit urbanitas intellegebat. Ea eam eros utroque vulputate, harum tation munere ea mea. Usu id postea mollis quaerendum, has oratio utroque</p>
      <p>Ei usu: Qualisque Suscipiantur</p>
      <p class="plain">Copyright © Company Name</p>
    </div>
  </footer>
</body>
</html>
```